We are looking for Facebook and Instagram templates. To use both platforms we will use square images. We need a template for our posts, not the header image.
Most posts contain multiple images and we need a designoverlay in which we can embed our images.
Attached a screenshot of our website www.velutra.be, our logo in svg and ai. The monkey is our mascotte (excact this monkey, not another).
We offer teambuildings, the style should be fun. Colors are antracite, limegreen and white. I did attache the current layout for posts but we are not happy with this.
If we could have some small design elements (like stickers) we can always create a new layout but is feels the same.
Our website is quite simple, this should also be in these post designs. Simple forms, rounded corners.
Updates

Allow more time for the designers, good work requires more time

Target Market(s)

Teambuilding

Industry/Entity Type

Teambuilding

Other font styles liked:
• RobotoSlab

Requirements
Must have
• If we could have some small design elements (like stickers) we can always create a new layout but is feels the same.
Should not have
• Complex design, simple images works best for us

```html
<!DOCTYPE html>
<html lang="nl">
<head>
<meta charset="utf-8">
<title>Velutra – social post templates</title>
<link rel="stylesheet" href="https://fonts.googleapis.com/css2?family=Bangers&family=Poppins:wght@400;500;600;700&display=swap">
<style>
  :root{
    --stage:#b9b9b9;
    --anthracite:#2e2f31;
    --anthracite-soft:#3a3b3e;
    --anthracite-deep:#242527;
    --lime:#a8cc0a;
    --lime-dark:#6c8f1f;
    --white:#ffffff;
    --paper:#f2f2f2;
    --leaf-grey:#d9d9d9;
  }
  *{box-sizing:border-box;margin:0;padding:0}
  html,body{width:1200px;height:2403px;overflow:hidden}
  body{background:var(--stage);position:relative;font-family:"Poppins",sans-serif}

  .post{position:absolute;left:125px;width:950px;height:950px;background:var(--anthracite);overflow:hidden;box-shadow:0 14px 36px rgba(0,0,0,.28)}
  .post--holiday{top:166px}
  .post--teambuilding{top:1288px}
  .post > *{position:absolute}

  .deco{position:absolute;left:0;top:0;width:950px;height:950px}

  .brand{display:flex;align-items:center;justify-content:center;background:#505153;border:3px solid var(--white);color:var(--white);font-family:"Poppins",sans-serif;font-weight:700;font-size:46px;letter-spacing:3px}

  .headline{font-family:"Bangers",sans-serif;line-height:1;letter-spacing:1px}
  .headline--lime{color:var(--lime)}
  .headline--white{color:var(--white)}

  .dots{height:6px;background-image:radial-gradient(circle,var(--lime) 2.6px,transparent 3px);background-size:16px 6px}

  .lead{color:var(--white);font-size:32px;line-height:41px;font-weight:400}

  .photo{border-radius:26px;padding:10px;overflow:hidden}
  .photo--lime{background:var(--lime)}
  .photo--white{background:var(--white)}
  .photo-fill{width:100%;height:100%;border-radius:18px}
  .fill-forest{background:linear-gradient(160deg,#4f6a3a 0%,#7d7a5c 55%,#a39175 100%)}
  .fill-field{background:linear-gradient(170deg,#4b5b3a 0%,#8d8a78 50%,#b4ab98 100%)}
  .fill-bar{background:linear-gradient(160deg,#3a2a22 0%,#8a5a3c 55%,#c9845c 100%)}
  .fill-archery{background:linear-gradient(165deg,#3f5d32 0%,#6b8646 55%,#a07a52 100%)}

  .mascot{background:var(--lime);border-radius:48% 52% 40% 45%}

  .sticker{display:flex;align-items:center;justify-content:center;text-align:center;font-family:"Bangers",sans-serif;color:var(--anthracite);line-height:.95}
  .sticker--play{width:116px;height:116px;border-radius:50%;background:var(--lime);border:5px solid var(--white);font-size:32px}

  .url{font-family:"Poppins",sans-serif;font-size:32px;font-weight:500;letter-spacing:11px;color:var(--anthracite)}
  .url b{color:var(--lime);font-weight:600}

  .tagline{font-family:"Poppins",sans-serif;font-weight:700;font-size:22px;color:var(--lime);letter-spacing:.3px}

  .features{display:flex;gap:16px;align-items:center}
  .feature{display:flex;align-items:center;gap:12px;font-size:13.5px;line-height:16px;color:var(--anthracite)}
  .feature-icon{width:44px;height:44px;border-radius:50%;border:3px solid var(--lime);display:flex;align-items:center;justify-content:center;flex:none}
</style>
</head>
<body>

<!-- Post 1: bouwverlof -->
<section class="post post--holiday">
  <svg class="deco" viewBox="0 0 950 950" aria-hidden="true">
    <path d="M520 0 C600 120 560 260 620 380 C680 520 660 660 720 760 L950 760 L950 0 Z" fill="var(--anthracite-soft)"/>
    <circle cx="0" cy="0" r="78" fill="var(--lime)" stroke="var(--white)" stroke-width="4"/>
    <circle cx="934" cy="440" r="58" fill="none" stroke="var(--white)" stroke-width="14"/>
    <circle cx="0" cy="632" r="52" fill="none" stroke="var(--lime)" stroke-width="16"/>
    <path d="M0 870 C120 820 220 800 340 790 C480 780 560 790 660 770 C760 750 860 760 950 740 L950 950 L0 950 Z" fill="var(--paper)" stroke="var(--lime)" stroke-width="8"/>
    <path d="M660 260 L672 290 L704 290 L678 308 L688 338 L660 320 L632 338 L642 308 L616 290 L648 290 Z" fill="none" stroke="var(--lime)" stroke-width="6"/>
    <path d="M628 388 L634 402 L649 402 L637 411 L642 425 L628 416 L614 425 L619 411 L607 402 L622 402 Z" fill="none" stroke="var(--white)" stroke-width="3"/>
    <path d="M336 690 C326 640 364 610 372 650 C382 700 420 720 440 670 C455 630 480 640 478 660" fill="none" stroke="var(--white)" stroke-width="3" stroke-dasharray="12 10"/>
    <path d="M468 652 L482 640 L490 656" fill="none" stroke="var(--white)" stroke-width="3"/>
    <path d="M500 0 C560 60 640 150 660 260 M560 170 C600 230 740 260 760 300" fill="none" stroke="var(--lime-dark)" stroke-width="20" opacity=".45" stroke-linecap="round"/>
    <path d="M10 330 C50 300 110 300 160 320" fill="none" stroke="var(--leaf-grey)" stroke-width="18" opacity=".55" stroke-linecap="round"/>
    <path d="M820 60 C860 30 910 20 950 20" fill="none" stroke="var(--leaf-grey)" stroke-width="18" opacity=".55" stroke-linecap="round"/>
    <path d="M780 880 C840 850 900 830 950 800 M10 930 C40 880 70 850 110 830" fill="none" stroke="var(--lime-dark)" stroke-width="22" opacity=".7" stroke-linecap="round"/>
  </svg>

  <div class="brand" style="left:69px;top:67px;width:288px;height:105px">VELUTRA</div>

  <h1 class="headline headline--lime" style="left:69px;top:252px;font-size:100px">INZET</h1>
  <h2 class="headline headline--white" style="left:66px;top:340px;font-size:108px">BOUWVERLOF</h2>
  <div class="dots" style="left:69px;top:466px;width:240px"></div>
  <p class="lead" style="left:69px;top:505px">Full house met de inzet van<br>de zomervakantie</p>

  <div class="photo photo--lime" style="left:664px;top:92px;width:262px;height:214px;transform:rotate(-9deg)">
    <div class="photo-fill fill-forest" role="img" aria-label="Groepsfoto van een team in kilts met vlaggen in het bos"></div>
  </div>
  <div class="photo photo--white" style="left:589px;top:292px;width:248px;height:230px;transform:rotate(5deg)">
    <div class="photo-fill fill-field" role="img" aria-label="Team bij touwtrekken op een zandveld"></div>
  </div>
  <div class="photo photo--lime" style="left:724px;top:478px;width:250px;height:218px;transform:rotate(-8deg)">
    <div class="photo-fill fill-bar" role="img" aria-label="Deelnemers samen aan de bar"></div>
  </div>

  <div class="sticker sticker--play" style="left:519px;top:586px">LET'S<br>PLAY</div>

  <div class="mascot" role="img" aria-label="Aapmascotte in limoengroen" style="left:62px;top:630px;width:270px;height:270px"></div>

  <p class="url" style="left:323px;top:852px">www.<b>velutra</b>.be</p>
</section>

<!-- Post 2: teambuilding -->
<section class="post post--teambuilding">
  <svg class="deco" viewBox="0 0 950 950" aria-hidden="true">
    <path d="M660 0 C620 120 700 260 760 360 C830 480 860 560 950 600 L950 0 Z" fill="var(--anthracite-soft)"/>
    <circle cx="0" cy="0" r="78" fill="var(--lime)" stroke="var(--white)" stroke-width="4"/>
    <circle cx="948" cy="537" r="58" fill="none" stroke="var(--lime)" stroke-width="16"/>
    <path d="M0 730 C150 740 260 770 300 800 L950 800 L950 950 L0 950 Z" fill="var(--lime)"/>
    <path d="M200 820 C400 800 600 790 800 800 L950 820 L950 950 L200 950 Z" fill="var(--white)"/>
    <path d="M48 505 L58 530 L86 530 L64 546 L72 572 L48 556 L24 572 L32 546 L10 530 L38 530 Z" fill="none" stroke="var(--lime)" stroke-width="6"/>
    <path d="M98 522 L103 534 L116 534 L106 542 L110 555 L98 547 L86 555 L90 542 L80 534 L93 534 Z" fill="none" stroke="var(--white)" stroke-width="3"/>
    <path d="M831 276 L843 306 L876 296 L858 324 L890 340 L856 348 L866 382 L836 364 L818 392 L812 358 L778 360 L802 336 L776 314 L810 310 Z" fill="var(--lime)" stroke="var(--white)" stroke-width="4"/>
    <path d="M262 760 C240 790 250 820 266 830 M285 786 L300 796 L290 810" fill="none" stroke="var(--white)" stroke-width="3" stroke-dasharray="8 7"/>
    <path d="M130 50 C170 70 250 120 290 170" fill="none" stroke="var(--lime-dark)" stroke-width="22" opacity=".55" stroke-linecap="round"/>
    <path d="M10 380 C60 350 140 360 200 390" fill="none" stroke="var(--leaf-grey)" stroke-width="20" opacity=".55" stroke-linecap="round"/>
    <path d="M820 80 C860 50 910 30 950 20" fill="none" stroke="var(--leaf-grey)" stroke-width="18" opacity=".55" stroke-linecap="round"/>
    <path d="M20 930 C40 880 80 840 160 820" fill="none" stroke="var(--lime-dark)" stroke-width="22" opacity=".6" stroke-linecap="round"/>
  </svg>

  <div class="brand" style="left:330px;top:68px;width:289px;height:103px">VELUTRA</div>

  <h1 class="headline headline--lime" style="left:122px;top:208px;font-size:64px">TEAMBUILDING MET COLLEGA'S,</h1>
  <h2 class="headline headline--white" style="left:0;width:950px;text-align:center;top:268px;font-size:62px">VRIENDEN OF FAMILIE</h2>

  <div class="sticker" style="left:792px;top:318px;width:80px;height:40px;font-size:30px">FUN</div>

  <div class="photo photo--white" style="left:174px;top:350px;width:298px;height:186px;transform:rotate(-1deg)">
    <div class="photo-fill fill-forest" role="img" aria-label="Groepsfoto van een team in kilts met vlaggen in het bos"></div>
  </div>
  <div class="photo photo--white" style="left:481px;top:355px;width:299px;height:181px;transform:rotate(1deg)">
    <div class="photo-fill fill-field" role="img" aria-label="Team bij touwtrekken op een zandveld"></div>
  </div>
  <div class="photo photo--white" style="left:169px;top:555px;width:303px;height:173px;transform:rotate(1deg)">
    <div class="photo-fill fill-bar" role="img" aria-label="Deelnemers samen aan de bar"></div>
  </div>
  <div class="photo photo--white" style="left:480px;top:565px;width:295px;height:168px;transform:rotate(-1deg)">
    <div class="photo-fill fill-archery" role="img" aria-label="Deelnemer bij boogschieten in het bos"></div>
  </div>

  <div class="mascot" role="img" aria-label="Aapmascotte in limoengroen" style="left:765px;top:672px;width:185px;height:230px"></div>

  <p class="tagline" style="left:326px;top:750px">BELEEF HET SAMEN BIJ VELUTRA</p>

  <div class="features" style="left:240px;top:840px">
    <div class="feature">
      <span class="feature-icon"><svg width="24" height="20" viewBox="0 0 24 20"><circle cx="8" cy="6" r="4" fill="var(--anthracite)"/><circle cx="17" cy="7" r="3" fill="var(--anthracite)"/><path d="M1 18 C1 12 15 12 15 18 Z M14 18 C14 13 23 13 23 18 Z" fill="var(--anthracite)"/></svg></span>
      <span>Voor bedrijven,<br>vrienden &amp; families</span>
    </div>
    <div class="feature">
      <span class="feature-icon"><svg width="22" height="20" viewBox="0 0 22 20"><path d="M11 1 L21 10 L18 10 L18 19 L13 19 L13 13 L9 13 L9 19 L4 19 L4 10 L1 10 Z" fill="var(--anthracite)"/></svg></span>
      <span>Unieke locatie<br>in de natuur</span>
    </div>
    <div class="feature">
      <span class="feature-icon"><svg width="24" height="24" viewBox="0 0 24 24"><circle cx="12" cy="12" r="10" fill="none" stroke="var(--anthracite)" stroke-width="2"/><circle cx="8.5" cy="9.5" r="1.5" fill="var(--anthracite)"/><circle cx="15.5" cy="9.5" r="1.5" fill="var(--anthracite)"/><path d="M7 14 C9 18 15 18 17 14" fill="none" stroke="var(--anthracite)" stroke-width="2"/></svg></span>
      <span>Plezier, verbinding<br>&amp; beleving</span>
    </div>
  </div>
</section>

</body>
</html>
```